Real Estate Sign to Help Modernize and Make it POP!

Design a sign style that would be good for marketing the sale or lease of properties. This will be 3 ' x 4' when printed and needs to look professional, modern, and catchy. It should us the company name, logo, and phone number at a minimum. Keep with the color scheme but open to varieties.

It will be printed and put in a large wooden frame as shown in one of the pictures.

Target Market(s)

Buyers and Tenants

Industry/Entity Type

Real Estate

Requirements
Must have
• company name, logo, and phone number
same color scheme as sign and website
Nice to have
• My Name, "Marlow Tefkin, CCIM"
Company Website
Ability to have an easy change from FOR SALE to FOR LEASE or FOR SALE/LEASE when I need to move this sign to a new property
An ability to have reflective colors printed on the contrast for cars to see at night
Should not have
• "Property Managed by"

```html
<!DOCTYPE html>
<html lang="en">
<head>
<meta charset="utf-8">
<title>Beacon Summit Realty – Property Sign</title>
<link rel="stylesheet" href="https://fonts.googleapis.com/css2?family=Tinos:wght@400;700&family=Abel&display=swap">
<style>
  :root {
    --sign-green: #4e5f57;
    --sage: #9bad87;
    --ink-navy: #2a2d3d;
    --paper: #ffffff;
    --backdrop: #f3f3f1;
    --serif: "Tinos", "Times New Roman", serif;
    --sans: "Abel", "Arial Narrow", sans-serif;
  }
  html, body {
    margin: 0;
    width: 901px;
    height: 1200px;
    overflow: hidden;
    background: var(--backdrop);
  }
  .sign {
    position: absolute;
    left: 30px;
    top: 285px;
    width: 841px;
    height: 629px;
    display: block;
    box-shadow: 0 4px 14px rgba(0,0,0,0.18);
  }
  .brand-name { font-family: var(--serif); font-weight: 400; fill: var(--sign-green); }
  .agent-name { font-family: var(--serif); font-size: 60px; fill: var(--paper); }
  .agent-title { font-family: var(--serif); font-weight: 700; font-size: 86px; fill: var(--sage); }
  .listing-status { font-family: var(--serif); font-size: 72px; fill: var(--ink-navy); }
  .listing-status .strong { font-weight: 700; }
  .listing-status .joiner { font-family: var(--sans); }
  .phone { font-family: var(--sans); font-size: 98px; fill: var(--paper); }
  .website { font-family: var(--sans); font-size: 62px; fill: var(--paper); }
</style>
</head>
<body>
<svg class="sign" viewBox="0 0 1032 772" xmlns="http://www.w3.org/2000/svg" aria-label="Beacon Summit Realty for sale or lease sign">
  <rect class="sign-board" width="1032" height="772" fill="var(--paper)"/>

  <g class="brand">
    <circle cx="225" cy="107" r="58" fill="var(--sign-green)"/>
    <text class="brand-name" x="328" y="140" font-size="90" letter-spacing="8">BEACON</text>
    <text class="brand-name" x="600" y="180" font-size="24" letter-spacing="9" text-anchor="middle">SUMMIT REALTY</text>
  </g>

  <g class="agent-dome">
    <path d="M230 274 C400 220 520 208 610 210 C800 214 960 322 1032 408" fill="none" stroke="var(--sign-green)" stroke-width="10"/>
    <path d="M28 424 C190 275 420 228 600 228 C790 230 950 330 1030 418 L1032 424 Z" fill="var(--sign-green)"/>
    <text class="agent-name" x="526" y="322" text-anchor="middle">Marlow Tefkin</text>
    <text class="agent-title" x="536" y="402" text-anchor="middle">CCIM</text>
  </g>

  <rect class="rule" x="0" y="427" width="1032" height="4" fill="var(--sign-green)"/>
  <text class="listing-status" x="528" y="510" text-anchor="middle">FOR <tspan class="strong">SALE</tspan> <tspan class="joiner">to</tspan> FOR <tspan class="strong">LEASE</tspan></text>
  <rect class="rule" x="0" y="528" width="1032" height="4" fill="var(--sign-green)"/>

  <rect class="contact-band" x="0" y="537" width="1032" height="235" fill="var(--sign-green)"/>
  <text class="phone" x="530" y="637" text-anchor="middle">(555) 214-7730</text>
  <text class="website" x="526" y="717" text-anchor="middle">www.beaconsummitrealty.com</text>
</svg>
</body>
</html>
```